Verlin Auto Repair - Flyer Design

My business is a automobile shop where we fix cars. Such things that we do but not limited to is brakes, Engine/Transmission change, Electrical work, emission test, oil change and automobile diagnostic. I am looking for a flyer that will catch peoples attention, I will be giving flyers to people, putting them in car windows and mailboxes. I am looking for a flier that will help to attract more customers to my business. I also want the flyer to say "Bring in your estimate from our competitors with this flyer and we will beat it by 10%" (does not have to be in those exact words). I also want the flyer to have my business address phone and operating hours. I have attached a business card and my business ad which I have placed in the newspaper before. I hope it helps with your design.
Industry/Entity Type
Car Repair
Look and feel
Each slider illustrates characteristics of the customer's brand and the style your logo design should communicate.

```html
<!DOCTYPE html>
<html lang="en">
<head>
<meta charset="utf-8">
<title>Verlin Auto Repair – Flyer</title>
<link rel="stylesheet" href="https://fonts.googleapis.com/css2?family=Anton&family=Titillium+Web:wght@300;400;700;900&display=swap">
<style>
:root{
  --page:#ffffff;
  --orange:#f6a41c;
  --orange-light:#f9b43a;
  --mono-head:#e2e2e2;
  --ink:#1a1a1a;
  --white:#ffffff;
  --red:#e8332c;
  --yellow:#ffe000;
  --band-dark:#3a3a3a;
  --band-light:#d9d9d7;
  --engine-dark:#1c1c1c;
  --engine-mid:#4a4a4a;
}
*{margin:0;padding:0;box-sizing:border-box}
html,body{width:1200px;height:1000px;overflow:hidden;background:var(--page)}
body{position:relative;font-family:"Titillium Web",sans-serif}
.flyer{position:absolute;top:77px;width:579px;height:820px;overflow:hidden;background:var(--engine-dark)}
.flyer--color{left:13px}
.flyer--mono{left:604px}

.flyer__photo{position:absolute;left:0;top:130px;width:579px;height:360px;
  background:linear-gradient(115deg,#5d6470 0%,#8a8f96 22%,#2f4a86 45%,#26407a 60%,#b7b9bc 78%,#6f747a 100%)}
.flyer__header{position:absolute;left:0;top:0;width:579px;height:200px}
.flyer__title{position:absolute;left:0;right:0;top:36px;text-align:center;font-weight:700;font-size:35px;letter-spacing:1.5px;line-height:1}
.flyer__tagline{position:absolute;left:0;right:0;top:88px;text-align:center;font-weight:700;font-size:15px;letter-spacing:2.4px;line-height:1}
.flyer--color .flyer__title,.flyer--color .flyer__tagline{color:#fff6e0}
.flyer--mono .flyer__title,.flyer--mono .flyer__tagline{color:var(--ink)}

.services{position:absolute;right:41px;top:206px;text-align:right;list-style:none;color:var(--white);font-weight:700;font-size:20px;line-height:23px;text-shadow:2px 2px 0 #000,-1px -1px 0 #000,1px -1px 0 #000,-1px 1px 0 #000}
.services li{margin-bottom:12px}

.estimate-band{position:absolute;left:0;top:485px;width:579px;height:66px;
  background:linear-gradient(to bottom,var(--band-dark) 0,#555 52%,var(--band-light) 52%,#c9c9c6 100%)}
.estimate-band__lead{position:absolute;left:56px;top:-7px;font-family:"Anton",sans-serif;font-size:70px;line-height:1;color:var(--red);letter-spacing:-1px;transform:scaleY(1.12);transform-origin:top}
.estimate-band__main{position:absolute;left:314px;top:-2px;font-family:"Anton",sans-serif;font-size:31px;line-height:1;color:var(--white);letter-spacing:.5px}
.estimate-band__sub{position:absolute;left:314px;top:36px;font-family:"Anton",sans-serif;font-size:21px;line-height:1;color:var(--ink);letter-spacing:.5px}

.flyer__engine{position:absolute;left:0;top:551px;width:579px;height:269px;
  background:radial-gradient(ellipse at 30% 40%,var(--engine-mid) 0,#2a2a2a 55%,var(--engine-dark) 100%)}

.offer{position:absolute;left:40px;top:585px;font-family:"Anton",sans-serif;color:var(--white);font-size:48px;line-height:1;white-space:nowrap}
.offer__pct{color:var(--yellow);font-size:62px;vertical-align:-4px}
.offer-icon{position:absolute;left:60px;top:636px}
.offer__label{position:absolute;left:166px;top:661px;width:182px;height:34px;background:var(--red);color:var(--white);font-weight:700;font-size:27px;line-height:34px;text-align:right;padding-right:4px}
.offer__note{position:absolute;right:233px;top:700px;text-align:right;color:var(--white);font-weight:300;font-size:29px;line-height:36px}

.info{position:absolute;left:373px;top:573px;width:178px;height:216px;border:2px dashed #e6e6e6;border-radius:8px;padding:8px 12px;color:var(--white)}
.info h3{color:var(--yellow);font-size:15px;font-weight:700;line-height:18px}
.info p{font-size:11px;line-height:15px}
.info__group{margin-bottom:10px}
</style>
</head>
<body>

<section class="flyer flyer--color">
  <div class="flyer__photo" role="img" aria-label="Photo of a smiling mechanic in blue overalls and cap giving a thumbs up over an open car engine"></div>
  <svg class="flyer__header" viewBox="0 0 579 200" aria-hidden="true">
    <path d="M0 0H579V170Q290 118 0 186Z" fill="var(--orange)"/>
    <path d="M0 186Q290 118 579 170" fill="none" stroke="#fff" stroke-width="4"/>
  </svg>
  <h1 class="flyer__title">VERLIN AUTO REPAIR</h1>
  <p class="flyer__tagline">SPECIALIZING IN FOREIGN &amp; DONESTIC CARS</p>
  <ul class="services">
    <li>BRAKES, ENGINE &amp;<br>TRANSMISSION<br>CHANGE</li>
    <li>ELECTRICAL WORK</li>
    <li>EMISSION TEST</li>
    <li>OIL CHANGE</li>
    <li>AUTOMOBILE<br>DIAGNOSTIC</li>
  </ul>
  <div class="flyer__engine" role="img" aria-label="Dark close-up photo of a car engine"></div>
  <div class="estimate-band">
    <span class="estimate-band__lead">BEATING</span>
    <span class="estimate-band__main">ANY ESTIMATE</span>
    <span class="estimate-band__sub">FROM ANY COMPANIES</span>
  </div>
  <p class="offer">GET <span class="offer__pct">10%</span> OFF</p>
  <svg class="offer-icon" width="110" height="110" viewBox="0 0 110 110" aria-hidden="true">
    <rect x="22" y="22" width="66" height="66" rx="10" transform="rotate(45 55 55)" fill="#f2c81a" stroke="#fff" stroke-width="3"/>
    <path d="M36 74L74 36M36 36L74 74" stroke="#222" stroke-width="9" stroke-linecap="round"/>
  </svg>
  <p class="offer__label">Any Repairs</p>
  <p class="offer__note">When You<br>Show This Flyer</p>
  <div class="info">
    <div class="info__group"><h3>Bring Us Your Car</h3><p>4127 S. Harlow Ave.<br>Brookfield IL. 60513</p></div>
    <div class="info__group"><h3>Contact Us</h3><p>(555) 418 - 7290<br>VerlinAutoRepair@mail.com</p></div>
    <div class="info__group"><h3>Operation Hours</h3><p>Monday - Friday : 8am - 5pm<br>Saturday : 8am - 1pm</p></div>
  </div>
</section>

<section class="flyer flyer--mono">
  <div class="flyer__photo" role="img" aria-label="Photo of a smiling mechanic in blue overalls and cap giving a thumbs up over an open car engine"></div>
  <svg class="flyer__header" viewBox="0 0 579 200" aria-hidden="true" role="img" aria-label="Faded grey photo of engine parts">
    <defs><linearGradient id="mono-head" x1="0" y1="0" x2="1" y2="1"><stop offset="0" stop-color="#d4d4d4"/><stop offset=".5" stop-color="#ededed"/><stop offset="1" stop-color="#c8c8c8"/></linearGradient></defs>
    <path d="M0 0H579V170Q290 118 0 186Z" fill="url(#mono-head)"/>
    <path d="M0 186Q290 118 579 170" fill="none" stroke="#fff" stroke-width="4"/>
  </svg>
  <h1 class="flyer__title">VERLIN AUTO REPAIR</h1>
  <p class="flyer__tagline">SPECIALIZING IN FOREIGN &amp; DONESTIC CARS</p>
  <ul class="services">
    <li>BRAKES, ENGINE &amp;<br>TRANSMISSION<br>CHANGE</li>
    <li>ELECTRICAL WORK</li>
    <li>EMISSION TEST</li>
    <li>OIL CHANGE</li>
    <li>AUTOMOBILE<br>DIAGNOSTIC</li>
  </ul>
  <div class="flyer__engine" role="img" aria-label="Dark close-up photo of a car engine"></div>
  <div class="estimate-band">
    <span class="estimate-band__lead">BEATING</span>
    <span class="estimate-band__main">ANY ESTIMATE</span>
    <span class="estimate-band__sub">FROM ANY COMPANIES</span>
  </div>
  <p class="offer">GET <span class="offer__pct">10%</span> OFF</p>
  <svg class="offer-icon" width="110" height="110" viewBox="0 0 110 110" aria-hidden="true">
    <rect x="22" y="22" width="66" height="66" rx="10" transform="rotate(45 55 55)" fill="#f2c81a" stroke="#fff" stroke-width="3"/>
    <path d="M36 74L74 36M36 36L74 74" stroke="#222" stroke-width="9" stroke-linecap="round"/>
  </svg>
  <p class="offer__label">Any Repairs</p>
  <p class="offer__note">When You<br>Show This Flyer</p>
  <div class="info">
    <div class="info__group"><h3>Bring Us Your Car</h3><p>4127 S. Harlow Ave.<br>Brookfield IL. 60513</p></div>
    <div class="info__group"><h3>Contact Us</h3><p>(555) 418 - 7290<br>VerlinAutoRepair@mail.com</p></div>
    <div class="info__group"><h3>Operation Hours</h3><p>Monday - Friday : 8am - 5pm<br>Saturday : 8am - 1pm</p></div>
  </div>
</section>

</body>
</html>
```